Verdane Metrics Systems Pte Ltd
Verdane Metrics Systems
Professional
Koren
Tabeli
No. 41, larchmoor Industrial Park E3, #05-22C
Singapore 648213
koren@vms-example.com.sg
www.vms-example.com.sg
209873561K
Business Card and Stationaries Design

```html
<!DOCTYPE html>
<html lang="en">
<head>
<meta charset="utf-8">
<title>Verdane Metrics Systems – Business Card</title>
<link href="https://fonts.googleapis.com/css2?family=Montserrat:wght@600&family=Open+Sans:wght@400;600;700&display=swap" rel="stylesheet">
<style>
  :root {
    --backdrop: #e9e6e1;
    --card-white: #ffffff;
    --card-black: #0d0d0d;
    --brand-blue: #1f6fb5;
    --band-dark: #163f6b;
    --ink: #3a3a3a;
    --muted: #666666;
  }
  * { margin: 0; padding: 0; box-sizing: border-box; }
  html, body { width: 1200px; height: 463px; overflow: hidden; }
  body {
    background: var(--backdrop);
    font-family: "Open Sans", Arial, sans-serif;
    position: relative;
  }
  .card {
    position: absolute;
    top: 112px;
    width: 490px;
    height: 333px;
    border-radius: 26px;
    overflow: hidden;
    box-shadow: 0 4px 12px rgba(0,0,0,0.18);
  }
  .card-front { left: 118px; background: var(--card-white); }
  .card-back { left: 640px; background: var(--card-black); }

  .brand {
    position: absolute;
    display: flex;
    align-items: center;
    gap: 12px;
    font-family: "Montserrat", Arial, sans-serif;
    font-weight: 600;
    color: var(--brand-blue);
  }
  .brand-square {
    width: 34px; height: 34px;
    background: var(--brand-blue);
    flex: none;
  }
  .brand-name { font-size: 26px; line-height: 1.05; letter-spacing: 0.5px; }
  .card-front .brand { left: 92px; top: 52px; }
  .card-back .brand { left: 100px; top: 136px; }

  .name-band {
    position: absolute;
    left: 0; right: 0; top: 145px;
    height: 16px;
    background: var(--brand-blue);
    border-bottom: 4px solid var(--band-dark);
  }
  .holder {
    position: absolute;
    top: 170px; left: 0; right: 0;
    text-align: center;
    font-weight: 700;
    font-size: 15px;
    color: var(--ink);
  }
  .address {
    position: absolute;
    right: 262px; top: 210px;
    text-align: right;
    font-size: 12px;
    line-height: 23px;
    color: var(--muted);
  }
  .contact {
    position: absolute;
    left: 248px; top: 233px;
    list-style: none;
    font-size: 12px;
    line-height: 23px;
    color: var(--muted);
  }
  .contact li { display: flex; align-items: center; gap: 6px; }
  .contact svg { width: 10px; height: 10px; flex: none; }
</style>
</head>
<body>
  <section class="card card-front">
    <div class="brand">
      <span class="brand-square"></span>
      <span class="brand-name">Verdane Metrics<br>Systems</span>
    </div>
    <div class="name-band"></div>
    <p class="holder">Koren Tabeli</p>
    <p class="address">No. 41,<br>larchmoor Industrial Park E3<br>#05-22C<br>Singapore 648213</p>
    <ul class="contact">
      <li>
        <svg viewBox="0 0 10 10"><circle cx="5" cy="5" r="5" fill="#666"/><rect x="2.2" y="3.2" width="5.6" height="3.6" fill="#fff"/><path d="M2.2 3.2 L5 5.3 L7.8 3.2" stroke="#666" stroke-width="0.7" fill="none"/></svg>
        koren@vms-example.com.sg
      </li>
      <li>
        <svg viewBox="0 0 10 10"><circle cx="5" cy="5" r="5" fill="#666"/><circle cx="5" cy="5" r="2.8" stroke="#fff" stroke-width="0.8" fill="none"/><path d="M2.2 5 H7.8 M5 2.2 V7.8" stroke="#fff" stroke-width="0.7"/></svg>
        www.vms-example.com.sg
      </li>
      <li>License No.: 209873561K</li>
    </ul>
  </section>

  <section class="card card-back">
    <div class="brand">
      <span class="brand-square"></span>
      <span class="brand-name">Verdane Metrics<br>Systems</span>
    </div>
  </section>
</body>
</html>
```